VELMIT Business Card

VELMIT (www.velmitpools.example) is a veteran in the swimming pool maintenance and repair business..we have served our clients for 15 years and have a research chemist, an electrician, a plumber and a pool building contractor (in part) on staff...We want to provide a business card that has a dual purpose, that people want to keep around, that leaves people speechless in the sense that they understand the mission of and the experience level of the TEAM at VELMIT.

Target Market(s)

persons who enjoy swimming and make it a priority to swim

Industry/Entity Type

Building

Font styles to use
Serif
Sans Serif

Colors
85acd3
3176b5
95b6d8
3276b5
0355a3
0555a3
0255a3
0455a3
85abd2

Requirements
Must have
• name, title, address, email, text
Nice to have
• a die cut shape
Should not have
• cartoons, pictures of pools

```html
<!DOCTYPE html>
<html lang="en">
<head>
<meta charset="utf-8">
<title>VELMIT Business Card</title>
<link rel="stylesheet" href="https://fonts.googleapis.com/css2?family=Exo+2:wght@400;500;600&display=swap">
<style>
  :root {
    --page-bg: #e9ecef;
    --card-bg: #ffffff;
    --brand-blue: #2ea3d5;
    --brand-deep: #1f86b8;
    --brand-light: #86d2f0;
    --ink: #2b3440;
    --ink-soft: #56606b;
    --on-brand: #ffffff;
  }
  * { box-sizing: border-box; margin: 0; padding: 0; }
  html, body {
    width: 1057px; height: 1200px; overflow: hidden;
    background: var(--page-bg);
    font-family: "Exo 2", sans-serif;
  }
  .sheet {
    width: 1057px; height: 1200px;
    display: flex; align-items: center; justify-content: center; gap: 44px;
  }
  .card {
    position: relative;
    width: 440px; height: 770px;
    background: var(--card-bg);
    overflow: hidden;
    box-shadow: 0 6px 22px rgba(0,0,0,0.14);
  }
  .brand { display: flex; flex-direction: column; align-items: center; }
  .brand-line { display: flex; align-items: center; gap: 12px; }
  .brand-mark { width: 30px; height: 30px; background: var(--brand-blue); }
  .brand-name {
    font-weight: 600; color: var(--brand-blue);
    letter-spacing: 2px; line-height: 1;
  }
  .brand-tagline {
    margin-top: 8px; color: var(--brand-blue);
    font-size: 15px; letter-spacing: 2.4px; font-weight: 500;
    white-space: nowrap;
  }
  .card--front .brand { position: absolute; top: 70px; right: 46px; }
  .card--front .brand-name { font-size: 60px; }
  .contact {
    position: absolute; top: 250px; left: 56px;
    list-style: none; color: var(--ink);
  }
  .contact-address { font-size: 17px; line-height: 1.45; margin-bottom: 12px; }
  .contact-row {
    display: flex; align-items: center; gap: 10px;
    font-size: 14px; color: var(--ink-soft); margin-bottom: 10px;
  }
  .contact-icon { width: 20px; height: 20px; flex: none; }
  .swoosh { position: absolute; left: 0; bottom: 0; width: 440px; height: 270px; }
  .swoosh-light { fill: var(--brand-light); }
  .swoosh-main { fill: var(--brand-blue); }
  .swoosh-edge { fill: var(--brand-deep); }
  .person {
    position: absolute; right: 40px; bottom: 70px;
    text-align: right; color: var(--on-brand); letter-spacing: 2px;
  }
  .person-name { font-size: 27px; font-weight: 500; }
  .person-title { font-size: 19px; margin-top: 6px; }
  .card--back .brand {
    position: absolute; top: 250px; left: 0; right: 0;
  }
  .card--back .brand-name { font-size: 66px; }
  .card--back .brand-tagline { font-size: 16px; }
  .back-web {
    position: absolute; left: 0; right: 0; bottom: 70px;
    text-align: center; color: var(--on-brand);
    font-size: 18px; letter-spacing: 1.5px;
  }
</style>
</head>
<body>
<main class="sheet">

  <section class="card card--front" aria-label="Card front">
    <div class="brand">
      <div class="brand-line">
        <span class="brand-mark"></span>
        <span class="brand-name">VELMIT</span>
      </div>
      <p class="brand-tagline">CLEARER WATER...EXPERTLY</p>
    </div>

    <ul class="contact">
      <li class="contact-address">42 Lagoon Drive,<br>Harbor Park West</li>
      <li class="contact-row">
        <svg class="contact-icon" viewBox="0 0 20 20"><rect width="20" height="20" rx="4" fill="var(--brand-blue)"/><path d="M6 4.5 L8.5 4.5 L9.3 7.5 L7.8 8.6 Q9 11.2 11.4 12.2 L12.5 10.7 L15.5 11.5 L15.5 14 Q15.5 15.5 14 15.5 Q5.5 15 4.5 6 Q4.5 4.5 6 4.5Z" fill="#fff"/></svg>
        <span>012 555 0147</span>
      </li>
      <li class="contact-row">
        <svg class="contact-icon" viewBox="0 0 20 20"><rect width="20" height="20" rx="4" fill="var(--brand-blue)"/><rect x="6" y="4" width="8" height="4" fill="#fff"/><rect x="4" y="8.5" width="12" height="5" rx="1" fill="#fff"/><rect x="6" y="12" width="8" height="4" fill="#fff" stroke="var(--brand-blue)" stroke-width="1"/></svg>
        <span>012 555 0148</span>
      </li>
      <li class="contact-row">
        <svg class="contact-icon" viewBox="0 0 20 20"><rect width="20" height="20" rx="4" fill="var(--brand-blue)"/><rect x="4" y="6" width="12" height="8" fill="#fff"/><path d="M4 6 L10 11 L16 6" fill="none" stroke="var(--brand-blue)" stroke-width="1.2"/></svg>
        <span>hello@velmitpools.example</span>
      </li>
      <li class="contact-row">
        <svg class="contact-icon" viewBox="0 0 20 20"><rect width="20" height="20" rx="4" fill="var(--brand-blue)"/><circle cx="10" cy="10" r="5.5" fill="none" stroke="#fff" stroke-width="1.4"/><path d="M4.5 10 H15.5 M10 4.5 Q7 10 10 15.5 M10 4.5 Q13 10 10 15.5" fill="none" stroke="#fff" stroke-width="1.1"/></svg>
        <span>www.velmitpools.example</span>
      </li>
    </ul>

    <svg class="swoosh" viewBox="0 0 440 270" aria-hidden="true">
      <path class="swoosh-light" d="M0 70 C140 10 320 20 440 110 L440 270 L0 270Z"/>
      <path class="swoosh-edge" d="M0 96 C150 36 320 50 440 140 L440 270 L0 270Z"/>
      <path class="swoosh-main" d="M0 110 C150 54 320 72 440 160 L440 270 L0 270Z"/>
    </svg>
    <div class="person">
      <p class="person-name">DANA REEVE</p>
      <p class="person-title">GENERAL MANAGER</p>
    </div>
  </section>

  <section class="card card--back" aria-label="Card back">
    <div class="brand">
      <div class="brand-line">
        <span class="brand-mark"></span>
        <span class="brand-name">VELMIT</span>
      </div>
      <p class="brand-tagline">CLEARER WATER...EXPERTLY</p>
    </div>

    <svg class="swoosh" viewBox="0 0 440 270" aria-hidden="true">
      <path class="swoosh-light" d="M0 70 C140 10 320 20 440 110 L440 270 L0 270Z"/>
      <path class="swoosh-edge" d="M0 96 C150 36 320 50 440 140 L440 270 L0 270Z"/>
      <path class="swoosh-main" d="M0 110 C150 54 320 72 440 160 L440 270 L0 270Z"/>
    </svg>
    <p class="back-web">www.velmitpools.example</p>
  </section>

</main>
</body>
</html>
```